Stonecrest Capital Partners
Business Cards
Project: Stonecrest Capital Partners
Stonecrest Capital Partners - Financial Services
Creative Brief
Simple
Marcus Delane
Managing Director
4625 Ridgeview Parkway Suite 200 Atlanta, GA 30341
Use 678-902-5148 Will supply updated number
mdelane@stonecrestcapital-example.com
www.stonecrestcapital-example.com
The will be business cards for Marcus Delane (Managing Director) and Victor Hollis (Managing Director). Address and phone numbers may change slightly this week. We are not sure if putting cell phones on yet. I once had a very simple business card in a basic font on high quality paper that looked great. Want very simple and professional. The logo can be on the front or keep the front simple and put the logo on the back.
Stonecrest LOGO attached (unless your design has it on the front)

```html
<!DOCTYPE html>
<html lang="en">
<head>
<meta charset="utf-8">
<title>Stonecrest Capital Partners – Business Cards</title>
<link href="https://fonts.googleapis.com/css2?family=Arimo:wght@400;700&display=swap" rel="stylesheet">
<style>
  :root {
    --bg: #eceff2;
    --card-white: #ffffff;
    --brand-blue: #1f7fc4;
    --brand-blue-dark: #135e9c;
    --brand-blue-light: #3fa3e0;
    --accent-green: #3aa845;
    --text-dark: #3a3f45;
    --text-mid: #6b7178;
  }
  * { margin: 0; padding: 0; box-sizing: border-box; }
  html, body {
    width: 1200px; height: 901px; overflow: hidden;
    background: var(--bg);
    font-family: "Arimo", Arial, sans-serif;
  }
  .sheet {
    position: relative; width: 1200px; height: 901px;
    display: flex; align-items: center; justify-content: center; gap: 40px;
  }
  .card {
    position: relative; width: 520px; height: 297px;
    border-radius: 14px; overflow: hidden;
    box-shadow: 0 10px 28px rgba(0,0,0,0.18);
  }
  /* Front */
  .card-front { background: var(--card-white); }
  .brand {
    position: absolute; left: 34px; top: 38px;
    display: flex; align-items: center; gap: 10px;
  }
  .brand-dot {
    width: 26px; height: 26px; border-radius: 50%;
    background: var(--brand-blue);
  }
  .brand-name {
    font-weight: 700; font-size: 22px; color: var(--brand-blue);
    letter-spacing: -0.3px;
  }
  .contact {
    position: absolute; left: 70px; top: 102px;
    color: var(--text-dark);
  }
  .contact-name { font-size: 20px; color: var(--brand-blue); }
  .contact-title { font-size: 11px; color: var(--text-mid); margin-top: 3px; }
  .contact-address { font-size: 10.5px; line-height: 1.45; margin-top: 8px; color: var(--text-mid); }
  .contact-lines { font-size: 10.5px; line-height: 1.5; margin-top: 8px; color: var(--text-mid); }
  .contact-lines .label { color: var(--accent-green); font-weight: 700; margin-right: 4px; }
  .web-band {
    position: absolute; right: 0; bottom: 26px;
    width: 222px; height: 26px;
    background: var(--accent-green);
    clip-path: polygon(18px 0, 100% 0, 100% 100%, 0 100%);
    color: #fff; font-size: 11.5px;
    display: flex; align-items: center; justify-content: flex-end; padding-right: 14px;
  }
  .base-band {
    position: absolute; left: 0; right: 0; bottom: 0; height: 26px;
    background: linear-gradient(90deg, var(--brand-blue-dark), var(--brand-blue));
  }
  /* Back */
  .card-back {
    background: linear-gradient(135deg, var(--brand-blue-light), var(--brand-blue) 50%, var(--brand-blue-dark));
  }
  .back-brand {
    position: absolute; right: 36px; top: 130px;
    display: flex; align-items: center; gap: 10px;
  }
  .back-brand .brand-dot { background: #fff; }
  .back-brand .brand-name { color: #fff; font-size: 26px; }
</style>
</head>
<body>
<main class="sheet">
  <section class="card card-front" aria-label="Business card front">
    <div class="brand">
      <span class="brand-dot"></span>
      <span class="brand-name">Stonecrest Capital Partners</span>
    </div>
    <div class="contact">
      <p class="contact-name">Marcus Delane</p>
      <p class="contact-title">Managing Director</p>
      <p class="contact-address">4625 Ridgeview Parkway<br>Suite 200<br>Atlanta, GA 30341</p>
      <p class="contact-lines">
        <span class="label">T</span>678-902-5148<br>
        <span class="label">E</span>mdelane@stonecrestcapital-example.com
      </p>
    </div>
    <div class="web-band">www.stonecrestcapital-example.com</div>
    <div class="base-band"></div>
  </section>

  <section class="card card-back" aria-label="Business card back">
    <div class="back-brand">
      <span class="brand-dot"></span>
      <span class="brand-name">Stonecrest</span>
    </div>
  </section>
</main>
</body>
</html>
```